High End Art Gallery Business Card

We're looking for a business card design that is elegant and artful. Foil embossing, blind embossed pattern, or some kind of "extra" element to make it stand out. Standard American size. The back should remain blank or nearly blank so that notes can be written on the back.
Please check our website at elsintandor.com to see information about our gallery and the type of artwork that we sell.
Included with the files is a brand identity guideline. In addition to the colors listed, we like to incorporate an indigo blue. The business card design in the guideline seems too simplistic. I have included some photos of other business card designs that have caught my eye.
thank you!

Contact Information for Business Card

Mirela Tandor
Gallery Owner
remaining details are in the attached docs

Requirements
Nice to have
• some kind of natural/organic element to reflect the hand-made nature of all of the original artwork.

```html
<!DOCTYPE html>
<html lang="en">
<head>
<meta charset="utf-8">
<title>Tandor Fine Art Gallery – Business Card</title>
<link href="https://fonts.googleapis.com/css2?family=Open+Sans:wght@400;600;700&display=swap" rel="stylesheet">
<style>
  :root {
    --backdrop: #2b2b2d;
    --paper: #fbfbf9;
    --gold: #c0994a;
    --ink: #4a4a4a;
    --ink-soft: #6f6f6f;
    --rule: #d8d8d4;
  }
  * { box-sizing: border-box; margin: 0; padding: 0; }
  html, body { width: 1200px; height: 900px; overflow: hidden; }
  body {
    background: var(--backdrop);
    font-family: "Open Sans", Arial, sans-serif;
    color: var(--ink);
    position: relative;
  }
  .card {
    position: absolute;
    width: 560px;
    height: 320px;
    background: var(--paper);
    box-shadow: 0 14px 30px rgba(0,0,0,.45);
  }
  .card--front { left: 250px; top: 100px; }
  .card--back  { left: 390px; top: 480px; }

  /* front */
  .brand {
    position: absolute;
    right: 36px;
    top: 34px;
    display: flex;
    flex-direction: column;
    align-items: flex-end;
    gap: 12px;
  }
  .brand__dot {
    width: 64px; height: 64px;
    border-radius: 50%;
    background: var(--gold);
    margin-right: 48px;
  }
  .brand__name {
    font-weight: 600;
    font-size: 15px;
    letter-spacing: 1.5px;
    text-transform: uppercase;
    color: var(--ink);
  }
  .gold-rule {
    position: absolute;
    left: 36px; right: 36px; top: 150px;
    height: 1px;
    background: var(--gold);
  }
  .person {
    position: absolute;
    left: 36px; top: 104px;
  }
  .person__name {
    font-weight: 700;
    font-size: 18px;
    letter-spacing: .8px;
    color: var(--gold);
    text-transform: uppercase;
    line-height: 1.1;
  }
  .person__role {
    font-size: 12px;
    letter-spacing: .6px;
    color: var(--ink);
    text-transform: uppercase;
    margin-top: 3px;
  }
  .contacts {
    position: absolute;
    left: 36px; top: 166px;
    list-style: none;
    font-size: 13px;
    color: var(--ink-soft);
    line-height: 20px;
  }
  .contacts li { display: flex; align-items: center; gap: 10px; }
  .contacts svg { width: 13px; height: 13px; fill: var(--gold); flex: none; }
  .grey-rule {
    position: absolute;
    left: 36px; right: 36px; top: 248px;
    height: 1px;
    background: var(--rule);
  }
  .address {
    position: absolute;
    left: 36px; top: 258px;
    font-size: 13px;
    color: var(--ink-soft);
  }

  /* back */
  .back__mark {
    position: absolute;
    left: 50%; top: 58px;
    width: 150px; height: 150px;
    margin-left: -75px;
    border-radius: 50%;
    border: 8px solid var(--gold);
  }
  .back__name {
    position: absolute;
    left: 0; right: 0; top: 224px;
    text-align: center;
    font-weight: 600;
    font-size: 14px;
    letter-spacing: 1.5px;
    text-transform: uppercase;
    color: var(--gold);
  }
  .back__web {
    position: absolute;
    left: 0; right: 0; bottom: 30px;
    text-align: center;
    font-size: 14px;
    letter-spacing: 4px;
    color: var(--ink-soft);
  }
</style>
</head>
<body>

  <section class="card card--front" aria-label="Business card front">
    <div class="brand">
      <span class="brand__dot" aria-hidden="true"></span>
      <span class="brand__name">Tandor Fine Art Gallery</span>
    </div>

    <div class="person">
      <p class="person__name">Mirela Tandor</p>
      <p class="person__role">Co-Owner</p>
    </div>

    <div class="gold-rule"></div>

    <ul class="contacts">
      <li>
        <svg viewBox="0 0 24 24" aria-hidden="true"><path d="M6.6 10.8a15.2 15.2 0 0 0 6.6 6.6l2.2-2.2a1 1 0 0 1 1-.25 11.4 11.4 0 0 0 3.6.57 1 1 0 0 1 1 1V20a1 1 0 0 1-1 1A17 17 0 0 1 3 4a1 1 0 0 1 1-1h3.5a1 1 0 0 1 1 1c0 1.25.2 2.45.57 3.57a1 1 0 0 1-.25 1z"/></svg>
        805-555-0142
      </li>
      <li>
        <svg viewBox="0 0 24 24" aria-hidden="true"><path d="M6 3h9l3 3v4h1a2 2 0 0 1 2 2v7a2 2 0 0 1-2 2H5a2 2 0 0 1-2-2v-7a2 2 0 0 1 2-2h1zm2 2v5h8V7h-2V5zm-1 9v2h2v-2zm4 0v2h2v-2zm4 0v2h2v-2z"/></svg>
        808-555-0178
      </li>
      <li>
        <svg viewBox="0 0 24 24" aria-hidden="true"><path d="M3 5h18a1 1 0 0 1 1 1v12a1 1 0 0 1-1 1H3a1 1 0 0 1-1-1V6a1 1 0 0 1 1-1zm1 2v.5l8 5 8-5V7l-8 5z"/></svg>
        info@elsintandor.com
      </li>
    </ul>

    <div class="grey-rule"></div>
    <p class="address">512 Kalena Street Honolulu, Hawaii 96814</p>
  </section>

  <section class="card card--back" aria-label="Business card back">
    <span class="back__mark" aria-hidden="true"></span>
    <p class="back__name">Tandor Fine Art Gallery</p>
    <p class="back__web">www.elsintandor.com</p>
  </section>

</body>
</html>
```